Incense Box and Outer Box Design

Require new package design with Die Lines for 6 fragrances: Dragon's Blood, Frankincense & Myrrh, Patchouli, Gentle Meadow, Dusk Tide, and White Sage.
25cm long incense sticks and 30x per box or tube.
We need really creative box design and solutions here. Not after standard box designs that all other incense sellers are doing.
Really need to think outside the "box" on this one.
Brand name is Kelvoro but this logo does NOT have to be prominent. There needs to be space for a GS1 barcode (which will be provided).

Target Market(s)

Yoga, Health, Religious

Font styles to use
Decorative

Requirements
Must have
• Classy and premium design. No tacky or cheap stock images or logo.\
Nice to have
• Bold, standout and bright.

Would love the cap or the box be an incense holder as well.
Should not have
• Cheap stock images

```html
<!DOCTYPE html>
<html lang="en">
<head>
<meta charset="utf-8">
<title>Kelvoro White Sage – Incense Box Panels</title>
<link rel="stylesheet" href="https://fonts.googleapis.com/css2?family=Open+Sans:wght@300;400;700&family=Oswald:wght@300;500&family=Great+Vibes&display=swap">
<style>
  :root {
    --bg-top: #b9b9b9;
    --bg-bottom: #f4f4f4;
    --panel-black: #141414;
    --side-black: #0e0e0e;
    --gold: #d9a93a;
    --gold-light: #f0c35a;
    --silver-light: #f2f2f2;
    --silver-mid: #a9a9a9;
    --silver-dark: #5c5c5c;
    --text-light: #dcdcdc;
    --text-muted: #b5b5b5;
    --band-dark: #1c1c1c;
    --band-mid: #4a4a4a;
  }
  * { margin: 0; padding: 0; box-sizing: border-box; }
  html, body { width: 900px; height: 1200px; overflow: hidden; }
  body {
    background: linear-gradient(to bottom, var(--bg-top), var(--bg-bottom) 70%);
    position: relative;
    font-family: "Open Sans", sans-serif;
  }
  .box-flat {
    position: absolute;
    left: 135px; top: 90px;
    width: 630px; height: 1020px;
    display: flex;
    box-shadow: 0 18px 40px rgba(0,0,0,0.25);
  }
  /* Side panel */
  .side-panel {
    width: 130px; height: 100%;
    background: var(--side-black);
    position: relative;
    color: var(--text-light);
    border-right: 1px solid #000;
  }
  .side-mark {
    position: absolute; left: 37px; top: 80px;
    width: 56px; height: 84px;
    background: linear-gradient(135deg, var(--gold-light), var(--gold));
  }
  .side-tagline {
    position: absolute; top: 215px; left: 0; width: 100%;
    text-align: center;
    font-family: "Oswald", sans-serif; font-weight: 300;
    font-size: 17px; line-height: 1.55; color: var(--text-light);
    letter-spacing: -0.3px;
  }
  .side-copy {
    position: absolute; top: 320px; left: 16px; width: 98px;
    font-family: "Oswald", sans-serif; font-weight: 300;
    font-size: 7.4px; line-height: 1.5; text-align: justify;
    hyphens: auto; color: var(--text-muted);
  }
  .side-band {
    position: absolute; left: 0; bottom: 0; width: 100%; height: 255px;
    background: linear-gradient(to bottom, #0e0e0e, #161616);
  }
  .side-url {
    position: absolute; bottom: 125px; left: 0; width: 100%; text-align: center;
    font-family: "Oswald", sans-serif; font-weight: 500;
    font-size: 17px; color: var(--text-light);
  }
  /* Front panel */
  .front-panel {
    width: 500px; height: 100%;
    background: var(--panel-black);
    position: relative;
    text-align: center;
  }
  .brand {
    position: absolute; top: 148px; left: 0; width: 100%;
    display: flex; justify-content: center; align-items: center; gap: 12px;
  }
  .brand-square {
    width: 58px; height: 58px;
    background: var(--gold);
  }
  .brand-name {
    font-family: "Open Sans", sans-serif; font-weight: 400;
    font-size: 44px; color: var(--gold); line-height: 1;
  }
  .product-name {
    position: absolute; top: 275px; left: 0; width: 100%;
    font-family: "Great Vibes", cursive; font-weight: 400;
    font-size: 116px; line-height: 0.92;
    background: linear-gradient(160deg, var(--silver-light) 15%, var(--silver-mid) 45%, #8a8a8a 60%, var(--silver-light) 85%);
    -webkit-background-clip: text; background-clip: text;
    color: transparent;
  }
  .product-name .line-one { display: block; margin-left: 40px; }
  .product-name .line-two { display: block; margin-left: -50px; }
  .product-type {
    position: absolute; top: 565px; left: 0; width: 100%;
    font-family: "Open Sans", sans-serif; font-weight: 300;
    font-size: 25px; line-height: 1.28; color: var(--text-light);
    letter-spacing: 0.3px;
  }
  .incense-art {
    position: absolute; top: 700px; left: 175px;
    width: 150px; height: 110px;
    background: radial-gradient(ellipse at center, #2e2e2e, var(--panel-black) 70%);
  }
  .metal-band {
    position: absolute; left: 0; bottom: 0; width: 100%; height: 255px;
    background:
      linear-gradient(90deg, var(--band-dark) 0%, var(--band-mid) 22%, #2a2a2a 45%, var(--band-mid) 70%, var(--band-dark) 100%);
    border-top: 1px solid #555;
  }
  .band-url {
    position: absolute; top: 100px; left: 0; width: 100%;
    font-family: "Open Sans", sans-serif; font-weight: 700;
    font-size: 24px; color: #f5f5f5;
  }
  .band-meta {
    position: absolute; top: 166px; left: 0; width: 100%;
    font-family: "Oswald", sans-serif; font-weight: 300;
    font-size: 12px; letter-spacing: 4px; color: var(--text-light);
  }
</style>
</head>
<body>
  <main class="box-flat">
    <section class="side-panel">
      <div class="side-mark"></div>
      <p class="side-tagline">PREMIUM<br>HERBAL<br>INCENSE STICKS</p>
      <p class="side-copy">Lorem Ipsum is simply dummy text of the printing and typesetting industry. Lorem Ipsum has been the industry's standard dummy text ever since the 1500s, when an unknown printer took a galley of type and scrambled it to make a type specimen book. It has survived not only five centuries, but also the leap into electronic typesetting, remaining essentially unchanged. It was popularised in the 1960s with the release of Quillset sheets containing Lorem Ipsum passages, and more recently with desktop publishing software like Folio Press including versions of Lorem Ipsum. Lorem Ipsum is simply dummy text of the printing and typesetting industry. Lorem Ipsum has been the industry's standard dummy text ever since the 1500s, when an unknown printer took a galley of type and scrambled it to make a type specimen book. It has survived not only five centuries, but also the leap into electronic typesetting, remaining essentially unchanged. It was popularised in the 1960s with the release of Quillset sheets containing Lorem Ipsum passages, and more recently with desktop publishing software like Folio Press including versions.</p>
      <div class="side-band"></div>
      <p class="side-url">kelvoro.com.au</p>
    </section>

    <section class="front-panel">
      <div class="brand">
        <span class="brand-square"></span>
        <span class="brand-name">Kelvoro</span>
      </div>
      <h1 class="product-name"><span class="line-one">White</span><span class="line-two">sage</span></h1>
      <p class="product-type">PREMIUM<br>HERBAL<br>INCENSE STICKS</p>
      <div class="incense-art" role="img" aria-label="Line illustration of a smoking incense stick resting in a curved holder"></div>
      <div class="metal-band">
        <p class="band-url">kelvoro.com.au</p>
        <p class="band-meta">250GRAM/8.8OZ &nbsp;|&nbsp; INCENSE BURNER</p>
      </div>
    </section>
  </main>
</body>
</html>
```